Louisiana personal injury attorney needs a postcard design

This will be the first of three post cards to go out to previous clients. We do not have intentions of making all three match/work with each other, but if you have an idea for that, please, let us know! This is for an attorney in Lafayette, LA that specializes in Medical Malpractice and Personal Injury. We would like the front of the post card to focus on those two practice areas and really grab someones attention!

the card in general will say: Glad to have served you, come see us for a free T-shirt, have a cup of coffee with us…

Please use a photo of the office for us to use on the back with a map of the office location (will send location when we pick the winner)

Industry/Entity Type

Legal

Font styles to use
Serif
Sans Serif

Requirements
Must have
• map of location of office. Large image or several images on the front. attention grabbing
Nice to have
• colors that match the logo. clean and easy to follow
Should not have
• should not be messy or too much going on.

```html
<!DOCTYPE html>
<html lang="en">
<head>
<meta charset="utf-8">
<title>Vantrelle Law Firm – Thank You Postcard</title>
<link rel="stylesheet" href="https://fonts.googleapis.com/css2?family=Playfair+Display:wght@500&family=Nunito+Sans:wght@400&display=swap">
<style>
  :root {
    --card: #f2f2f2;
    --gold: #c4952f;
    --slate: #666666;
    --ink: #555555;
    --photo-light: #8a8a8a;
    --photo-dark: #3a3a3a;
    --text-on-gold: #f7f3ea;
  }
  * { margin: 0; padding: 0; box-sizing: border-box; }
  html, body {
    width: 1200px;
    height: 901px;
    overflow: hidden;
    background: var(--card);
  }
  .postcard {
    position: relative;
    width: 1200px;
    height: 901px;
    background: var(--card);
  }
  .brand {
    position: absolute;
    top: 62px;
    right: 59px;
    display: flex;
    align-items: center;
    gap: 10px;
    font-family: "Nunito Sans", sans-serif;
    font-weight: 400;
    color: var(--gold);
  }
  .brand-mark {
    width: 12px;
    height: 12px;
    background: var(--gold);
  }
  .brand-name {
    display: flex;
    flex-direction: column;
    align-items: flex-end;
    line-height: 1;
  }
  .brand-name .firm { font-size: 30px; letter-spacing: 0.04em; }
  .brand-name .practice { font-size: 17px; letter-spacing: 0.3em; margin-top: 6px; margin-right: -0.3em; }
  .hero-photo {
    position: absolute;
    left: 64px;
    top: 64px;
    width: 682px;
    height: 765px;
    background: radial-gradient(ellipse at 40% 45%, var(--photo-light) 0%, #5c5c5c 45%, var(--photo-dark) 100%);
  }
  .headline-panel {
    position: absolute;
    left: 653px;
    top: 260px;
    width: 486px;
    height: 455px;
    background: var(--gold);
  }
  .headline {
    position: absolute;
    right: 26px;
    top: 22px;
    font-family: "Playfair Display", serif;
    font-weight: 500;
    font-size: 100px;
    line-height: 98px;
    letter-spacing: -0.01em;
    text-align: right;
    color: var(--text-on-gold);
  }
  .pointer {
    position: absolute;
    left: 0;
    top: 0;
    width: 1200px;
    height: 901px;
    z-index: 2;
  }
  .invitation {
    position: absolute;
    left: 800px;
    top: 750px;
    font-family: "Nunito Sans", sans-serif;
    font-size: 26px;
    line-height: 40px;
    letter-spacing: 0.02em;
    color: var(--ink);
    white-space: nowrap;
  }
  .invitation span { display: block; }
</style>
</head>
<body>
  <main class="postcard">
    <div class="brand">
      <span class="brand-mark" aria-hidden="true"></span>
      <span class="brand-name">
        <span class="firm">VANTRELLE</span>
        <span class="practice">LAW FIRM</span>
      </span>
    </div>

    <div class="hero-photo" role="img" aria-label="Black and white photo of a wooden judge's gavel resting on its block beside a stethoscope"></div>

    <section class="headline-panel">
      <h1 class="headline">Glad<br>to have<br>served<br>you</h1>
    </section>

    <svg class="pointer" viewBox="0 0 1200 901" aria-hidden="true">
      <polygon points="746,669 710,752 781,750" fill="var(--slate)"/>
    </svg>

    <p class="invitation">
      <span>come see us for a free T-shirt,</span>
      <span>have a cup of coffee with us…</span>
    </p>
  </main>
</body>
</html>
```